Personal Real Estate Wordpress Site

I like to create a design that is similar to

http://www.thecorvellsiblings.example

with your creativity and given the images I provide, help to see what fits best in terms of the overall feel. color theme can be similar and use the attached pictures and if not sufficient, you may see what is suitable.

Target Market(s)

Consumers for singapore market

Industry/Entity Type

Real Estate

Font styles to use
Sans Serif

Colors
0456a4

Requirements
Must have
• Very similar feel and design to the attached website for reference. Can try similar colour tone
Nice to have
• clean lines and any unique features
Should not have
• boring traditional template. just see the reference website will do

```html
<!DOCTYPE html>
<html lang="en">
<head>
<meta charset="utf-8">
<title>Nova Homes — Singapore Real Estate</title>
<link href="https://fonts.googleapis.com/css2?family=Roboto:wght@400;500;700&display=swap" rel="stylesheet">
<style>
:root{
  --crimson:#9b0c38;
  --crimson-dark:#7c0029;
  --red:#d7112f;
  --blue:#1d4f91;
  --ink:#222;
  --muted:#555;
  --line:#d8d8d8;
  --footer:#1c1c1c;
  --footer-bottom:#111;
  --soft:#f2f2f2;
}
*{box-sizing:border-box;margin:0;padding:0}
html,body{width:1200px;height:4876px;overflow:hidden}
body{font-family:"Roboto",sans-serif;color:var(--ink);background:#fff;position:relative;font-size:13px}
.abs{position:absolute}
section,header,footer{position:absolute;left:0;width:1200px}
.btn{display:inline-block;background:var(--red);color:#fff;font-weight:500;font-size:14px;text-align:center;border-radius:4px}
.h2{color:var(--blue);font-weight:500;font-size:30px}
p.body{font-size:13px;line-height:19px;color:var(--ink)}

/* top bar */
.topbar{top:0;height:38px;background:#fff;font-size:13px;color:#333}
.topbar .contact{left:119px;top:11px}
.topbar .contact span{margin-right:22px}
.social{display:flex;gap:8px}
.social i{width:18px;height:18px;border-radius:50%;display:block}
.topbar .social{left:528px;top:10px}
.topbar .social i:first-child{background:var(--red)}
.topbar .social i{border:1.5px solid #333}
.topbar .social i:first-child{border-color:var(--red)}
.topbar .account{right:119px;top:11px}
.topbar .account span{margin-left:18px}

/* hero */
.hero{top:38px;height:681px;background:linear-gradient(180deg,#cfd3d6 0%,#8d9499 35%,#4d5559 70%,#2d3133 100%)}
.nav{top:62px;left:0;width:1200px;font-size:13px;color:#222}
.nav a{position:absolute;top:0;color:#222;text-decoration:none}
.nav a.active{color:var(--red)}
.brand{position:absolute;display:flex;align-items:center;gap:6px;font-weight:700;color:var(--blue)}
.brand i{display:block;background:var(--red)}
.hero .brand{left:556px;top:-4px;font-size:28px}
.hero .brand i{width:18px;height:18px}
.hero h1{position:absolute;top:305px;width:1200px;text-align:center;color:#fff;font-weight:400;font-size:30px}

/* search */
.search{top:719px;height:190px;background:var(--crimson)}
.search .field{left:119px;top:43px;width:797px;height:35px;background:var(--crimson-dark);border-radius:3px;color:#fff;font-size:12px;padding:11px 18px}
.search .go{left:929px;top:43px;width:152px;height:35px;line-height:35px;border-radius:3px;font-size:12px}
.filters{left:119px;top:97px;width:962px;height:38px;color:#fff;font-size:12px}
.filters .lbl{position:absolute;top:12px}
.filters .sel{position:absolute;top:3px;height:34px;background:var(--crimson-dark);border-radius:3px;padding:10px 14px}
.filters .sel:after{content:"";position:absolute;right:12px;top:14px;border:5px solid transparent;border-top:6px solid #fff}

/* about */
.about{top:909px;height:640px}
.about .h2{left:119px;top:160px;font-size:31px}
.about .txt{left:119px;top:226px;width:440px}
.about .txt p+p{margin-top:18px}
.about .btn{left:119px;top:384px;width:157px;height:38px;line-height:38px}

/* properties */
.props{top:1549px;height:547px}
.props .h2{top:10px;width:1200px;text-align:center}
.arrows{display:flex;gap:6px}
.arrows i{width:21px;height:21px;border-radius:50%;display:block;background:var(--red);position:relative}
.arrows i:after{content:"";position:absolute;left:8px;top:6px;width:5px;height:5px;border-left:2px solid #fff;border-bottom:2px solid #fff;transform:rotate(45deg)}
.arrows i.next{background:var(--crimson-dark)}
.arrows i.next:after{left:5px;transform:rotate(-135deg)}
.props .arrows{left:1031px;top:19px}
.card{position:absolute;top:88px;width:305px;height:381px;border:1px solid var(--line)}
.card .photo{height:208px;background:linear-gradient(160deg,#cfe0ee,#8aa6bd 55%,#5f6d72)}
.card .tag{position:absolute;left:75px;top:190px;width:155px;height:34px;line-height:34px;border-radius:4px}
.card .title{position:absolute;left:12px;top:236px;font-weight:500;font-size:13px}
.card .likes{position:absolute;right:14px;top:233px;font-size:16px;color:#444}
.card .desc{position:absolute;left:12px;top:258px;width:280px;font-size:12.5px;line-height:19px;color:#444}
.card .price{position:absolute;left:0;width:100%;top:314px;text-align:center;font-size:22px;color:var(--blue)}
.card .price sup{font-size:12px;vertical-align:top}
.card .specs{position:absolute;left:0;bottom:0;width:100%;height:30px;border-top:1px solid var(--line);font-size:12px;color:#444}
.card .specs span{position:absolute;top:9px}

/* app */
.app{top:2096px;height:554px;background:var(--crimson);color:#fff}
.phones{position:absolute;left:160px;top:78px;width:380px;height:514px;border-radius:36px;background:linear-gradient(150deg,#fafafa,#d6d6d6 60%,#b3b3b3)}
.app h2{position:absolute;left:619px;top:126px;font-weight:500;font-size:30px}
.app .copy{position:absolute;left:619px;top:188px;width:462px;font-size:13px;line-height:19px;font-weight:500}
.app .copy p+p{margin-top:14px}
.store{position:absolute;top:366px;width:224px;height:66px;background:#000;border:2px solid #fff;border-radius:8px}

/* agent */
.agent{top:2773px;height:340px}
.agent .name{left:119px;top:24px;display:flex;align-items:center;gap:12px;font-size:26px;letter-spacing:2px;color:#111;line-height:28px}
.agent .name i{display:block;width:30px;height:30px;border:1.5px solid #111}
.agent .txt{left:119px;top:112px;width:440px}
.agent .txt p+p{margin-top:18px}
.agent .btn{left:119px;top:262px;width:157px;height:38px;line-height:38px}
.team{position:absolute;left:600px;top:0;width:500px;height:323px;background:linear-gradient(180deg,#f7f7f7,#e9e9e9 60%,#d6d6d6)}

/* testimonials & blogs */
.tb{top:3150px;height:580px}
.tb .h2{top:22px;text-align:center;width:480px}
.tb .arrows{left:1031px;top:32px}
.testi{position:absolute;left:119px;top:106px;width:461px;height:444px;background:#f1f1f1;padding:12px}
.testi .inner{background:#fff;width:100%;height:100%;position:relative;text-align:center}
.testi .avatar{position:absolute;left:162px;top:22px;width:110px;height:110px;border-radius:50%;background:linear-gradient(160deg,#dfe5ea,#8ea0ad)}
.testi .who{position:absolute;top:142px;width:100%;font-size:16px;color:#333}
.testi .role{position:absolute;top:162px;width:100%;font-size:13px;color:var(--red)}
.testi .quote{position:absolute;left:90px;top:204px;width:258px;font-size:13px;line-height:17px;color:#555}
.testi .q{position:absolute;font-size:34px;color:#555;font-family:Georgia,serif}
.testi .more{position:absolute;top:270px;width:100%;font-size:13px;color:#777}
.dots{position:absolute;top:310px;width:100%;display:flex;justify-content:center;gap:7px}
.dots i{width:6px;height:6px;border-radius:50%;background:#aaa}
.dots i:first-child{background:var(--red)}
.testi .btn{position:absolute;left:140px;top:344px;width:157px;height:38px;line-height:38px}
.post{position:absolute;left:604px;width:477px;height:212px;background:#f1f1f1}
.post .photo{position:absolute;left:12px;top:12px;width:221px;height:188px;background:linear-gradient(170deg,#d6dde4,#6f7a83 60%,#2b2f33)}
.post .t{position:absolute;left:248px;top:12px;font-weight:500;font-size:13px;color:#444;letter-spacing:.5px}
.post .date{position:absolute;left:248px;top:32px;font-size:12px;color:#444}
.post .c{position:absolute;right:14px;top:34px;font-size:12px;color:#444}
.post .x{position:absolute;left:248px;top:56px;width:218px;font-size:12.5px;line-height:17px;color:#555}
.post .x p+p{margin-top:8px}
.post .m{position:absolute;left:248px;top:182px;font-size:13px;color:#555}

/* seen on */
.seen{top:3760px;height:240px}
.seen .h2{top:10px;width:1200px;text-align:center}
.seen .arrows i{position:absolute;top:138px}
.partner{position:absolute;top:83px;width:182px;height:117px;background:var(--soft)}
.partner i{position:absolute;left:51px;top:40px;width:80px;height:36px;border-radius:4px;background:#c9ccd2}

/* quick contact */
.qc{top:4066px;height:435px;background:var(--crimson)}
.qc h2{position:absolute;left:119px;top:93px;color:#fff;font-weight:500;font-size:30px}
.qc .f{position:absolute;height:36px;background:var(--crimson-dark);color:#fff;font-size:12px;font-weight:500;padding:12px 14px}
.qc .btn{position:absolute;left:119px;top:344px;width:155px;height:38px;line-height:38px;font-size:13px}
.map{position:absolute;left:600px;top:0;width:600px;height:435px;background:linear-gradient(135deg,#ececec,#dcdfe2 55%,#e7e7e3)}

/* footer */
.footer{top:4501px;height:307px;background:var(--footer);color:#fff}
.footer .brand{left:119px;top:52px;font-size:28px;color:var(--red)}
.footer .brand i{width:18px;height:18px;background:var(--blue)}
.footer .about-f{position:absolute;left:119px;top:162px;width:210px;font-size:12.5px;line-height:17px;font-weight:500}
.footer .rm{position:absolute;left:119px;top:218px;font-size:11px}
.footer h4{position:absolute;top:94px;font-weight:500;font-size:17px}
.footer ul{position:absolute;left:395px;top:149px;font-size:12.5px;line-height:16px;font-weight:500}
.footer .addr{position:absolute;left:572px;top:142px;font-size:12.5px;line-height:23px;font-weight:500}
.footer .addr div{position:relative;padding-left:34px}
.footer .addr svg{position:absolute;left:0;top:5px}
.footer .sub-l{position:absolute;left:847px;top:142px;font-size:11px;font-weight:500}
.footer .sub{position:absolute;left:849px;top:174px;width:230px;height:26px;border:1px solid #fff;border-radius:14px;font-size:11px;padding:6px 16px}
.footer .sub b{position:absolute;right:-1px;top:-1px;width:74px;height:26px;border-radius:14px;background:var(--red);font-weight:500;text-align:center;line-height:26px}
.footer .social{position:absolute;left:850px;top:220px}
.footer .social i{background:#fff;width:22px;height:22px}
.footer .social i:first-child{background:var(--red)}
.bottom{top:4808px;height:68px;background:var(--footer-bottom);color:#fff;font-size:13px;font-weight:500}
.bottom span{position:absolute;top:24px}
</style>
</head>
<body>

<header class="topbar">
  <div class="abs contact"><span>&#9742; +65 6100 2200</span><span>&#9993; hello@novahomes.example</span></div>
  <div class="abs social"><i></i><i></i><i></i><i></i><i></i></div>
  <div class="abs account"><span>Login</span><span>| &nbsp;Register</span></div>
</header>

<section class="hero">
  <div class="abs" role="img" aria-label="Aerial photograph of the Singapore city skyline and waterfront stadium" style="inset:0"></div>
  <nav class="abs nav">
    <a class="active" style="left:119px">Home</a>
    <a style="left:212px">Features Properties</a>
    <a style="left:393px">Sell</a>
    <a style="left:470px">Buy</a>
    <div class="brand"><i></i>NOVA</div>
    <a style="left:684px">Find an Agent</a>
    <a style="left:813px">Testimonials</a>
    <a style="left:939px">Blogs</a>
    <a style="left:1015px">Contact us</a>
  </nav>
  <h1>To, This is Singapore's Skyline</h1>
  <svg class="abs" style="left:582px;top:355px" width="38" height="38" viewBox="0 0 38 38"><circle cx="19" cy="19" r="16" fill="none" stroke="#fff" stroke-width="3"/><path d="M15 12 L26 19 L15 26Z" fill="#fff"/></svg>
</section>

<section class="search">
  <div class="abs field">Enter City, Neighborhood, ZIP, Address, or MLS #</div>
  <div class="abs btn go">Search &#9906;</div>
  <div class="abs filters">
    <span class="lbl" style="left:0">Price From</span>
    <div class="sel" style="left:95px;width:215px">Any</div>
    <span class="lbl" style="left:353px">To</span>
    <div class="sel" style="left:381px;width:215px">Any</div>
    <span class="lbl" style="left:595px;left:595px">Beds</span>
    <div class="sel" style="left:645px;width:90px">Any</div>
    <span class="lbl" style="left:757px">Baths</span>
    <div class="sel" style="left:812px;width:150px">Any</div>
  </div>
</section>

<section class="about">
  <h2 class="abs h2">About us</h2>
  <div class="abs txt">
    <p class="body">Lorem Ipsum is simply dummy text of the printing and typesetting industry. Lorem Ipsum has been the industry's standard dummy text ever since the 1500s,</p>
    <p class="body">when an unknown printer took a galley of type and scrambled it to make a type specimen book. It has survived not only five centuries,</p>
  </div>
  <a class="abs btn">View More</a>
  <svg class="abs" style="left:604px;top:62px" width="516" height="546" viewBox="0 0 516 546">
    <polygon points="258,0 516,250 258,546 0,250" fill="var(--crimson)"/>
    <polygon points="258,120 400,250 258,430 116,250" fill="#fff"/>
    <polygon points="258,0 292,34 34,250 0,250" fill="var(--red)"/>
  </svg>
  <div class="abs" role="img" aria-label="Portrait of the lead agent in a dark suit seated on a stool" style="left:640px;top:80px;width:240px;height:540px;background:linear-gradient(180deg,#d9dde2,#3a4150 45%,#1c1f27);border-radius:110px 110px 10px 10px"></div>
</section>

<section class="props">
  <h2 class="abs h2">Exclusive Properties</h2>
  <div class="abs arrows"><i></i><i class="next"></i></div>
  <div class="card" style="left:119px">
    <div class="photo" role="img" aria-label="Modern white villa with glass facade"></div>
    <a class="btn tag">Details</a>
    <span class="title">Singapore City Highlights</span><span class="likes">&#9825; 25</span>
    <p class="desc">Lorem Ipsum is simply dummy text of the printing and typesetting industry.</p>
    <div class="price"><sup>S</sup> 710</div>
    <div class="specs"><span style="left:12px">3 Rooms</span><span style="left:124px">4 Beds</span><span style="right:16px">234 SQFT</span></div>
  </div>
  <div class="card" style="left:448px">
    <div class="photo" role="img" aria-label="Contemporary house with timber screens at dusk"></div>
    <a class="btn tag">Details</a>
    <span class="title">Singapore City Highlights</span><span class="likes">&#9825; 25</span>
    <p class="desc">Lorem Ipsum is simply dummy text of the printing and typesetting industry.</p>
    <div class="price"><sup>S</sup> 810</div>
    <div class="specs"><span style="left:12px">3 Rooms</span><span style="left:124px">4 Beds</span><span style="right:16px">234 SQFT</span></div>
  </div>
  <div class="card" style="left:777px">
    <div class="photo" role="img" aria-label="Row of modern townhouses"></div>
    <a class="btn tag">Details</a>
    <span class="title">Singapore City Highlights</span><span class="likes">&#9825; 25</span>
    <p class="desc">Lorem Ipsum is simply dummy text of the printing and typesetting industry.</p>
    <div class="price"><sup>S</sup> 790</div>
    <div class="specs"><span style="left:12px">3 Rooms</span><span style="left:124px">4 Beds</span><span style="right:16px">234 SQFT</span></div>
  </div>
</section>

<section class="app">
  <div class="phones" role="img" aria-label="Two smartphones showing the property search app"></div>
  <h2>The NOVA Real Estate App</h2>
  <div class="copy">
    <p>Search for a house. See how much homes are selling for in your neighborhood.</p>
    <p>The NOVA Mobile App puts that information in your hand - anytime, anywhere. The only real estate app that works on standard cell phones, smartphones, and tablets alike, the NOVA Mobile App puts the power to search and find exactly what you're looking for in your hands.</p>
  </div>
  <div class="store" style="left:619px"></div>
  <div class="store" style="left:857px"></div>
</section>

<section class="agent">
  <div class="abs name"><i></i><span>KAEL<br>MARLOW</span></div>
  <div class="abs txt">
    <p class="body">Lorem Ipsum is simply dummy text of the printing and typesetting industry. Lorem Ipsum has been the industry's standard dummy text ever since the 1500s,</p>
    <p class="body">when an unknown printer took a galley of type and scrambled it to make a type specimen book. It has survived not only five centuries,</p>
  </div>
  <a class="abs btn">View More</a>
  <div class="team" role="img" aria-label="Group photo of the agency team in dark suits and red ties"></div>
</section>

<section class="tb">
  <h2 class="abs h2" style="left:119px">Testimonials</h2>
  <h2 class="abs h2" style="left:604px">Blogs</h2>
  <div class="abs arrows"><i></i><i class="next"></i></div>
  <div class="testi"><div class="inner">
    <div class="avatar" role="img" aria-label="Client portrait"></div>
    <div class="who">Dorian Vale</div>
    <div class="role">Creative Director</div>
    <span class="q" style="left:78px;top:180px">&ldquo;</span>
    <p class="quote">Lorem Ipsum is simply dummy text of the printing and typesetting .Lorem Ipsum industry.</p>
    <span class="q" style="left:340px;top:232px">&rdquo;</span>
    <div class="more">Read More.. &#8853;</div>
    <div class="dots"><i></i><i></i><i></i></div>
    <a class="btn">View More</a>
  </div></div>
  <div class="post" style="top:106px">
    <div class="photo" role="img" aria-label="Modern house lit at night"></div>
    <span class="t">BLOG POST TITLE</span><span class="date">&#9638; 05 Oct , 2018</span><span class="c">&#9711; 20</span>
    <div class="x"><p>Lorem Ipsum is simply dummy text of the And printing matter and typesetting industry.</p><p>Ipsum is simply dummy text of the And printing matter and type setting industry.</p></div>
    <span class="m">Read More..&#8853;</span>
  </div>
  <div class="post" style="top:336px">
    <div class="photo" role="img" aria-label="Glass and timber building at dusk"></div>
    <span class="t">BLOG POST TITLE</span><span class="date">&#9638; 05 Oct , 2018</span><span class="c">&#9711; 20</span>
    <div class="x"><p>Lorem Ipsum is simply dummy text of the And printing matter and typesetting industry.</p><p>Ipsum is simply dummy text of the And printing matter and type setting industry.</p></div>
    <span class="m">Read More..&#8853;</span>
  </div>
</section>

<section class="seen">
  <h2 class="abs h2">AS SEEN ON</h2>
  <div class="arrows"><i style="left:50px"></i><i class="next" style="left:1130px"></i></div>
  <div class="partner" style="left:119px"><i></i></div>
  <div class="partner" style="left:314px"><i></i></div>
  <div class="partner" style="left:510px"><i></i></div>
  <div class="partner" style="left:705px"><i></i></div>
  <div class="partner" style="left:899px"><i></i></div>
</section>

<section class="qc">
  <h2>Quick Contact</h2>
  <div class="f" style="left:119px;top:146px;width:204px">First Name</div>
  <div class="f" style="left:333px;top:146px;width:207px">Last Name</div>
  <div class="f" style="left:119px;top:192px;width:204px">Email</div>
  <div class="f" style="left:333px;top:192px;width:207px">Phone</div>
  <div class="f" style="left:119px;top:238px;width:421px;height:92px">Message</div>
  <a class="btn">View All</a>
  <div class="map" role="img" aria-label="Street map of the office neighbourhood with location pins"></div>
</section>

<footer class="footer">
  <div class="brand"><i></i>NOVA</div>
  <p class="about-f">Lorem Ipsum is simply dummy text of the printing and typese tting industry.</p>
  <span class="rm">Read More.. &#8853;</span>
  <h4 style="left:369px">Quick Link</h4>
  <ul>
    <li>Home</li><li>Freture Properties</li><li>Sell</li><li>Buy</li><li>Testimonials</li><li>Blogs</li><li>Contact us</li>
  </ul>
  <h4 style="left:573px">Quick Contact</h4>
  <div class="addr">
    <div><svg width="10" height="13" viewBox="0 0 10 13"><path d="M5 0a5 5 0 0 1 5 5c0 4-5 8-5 8S0 9 0 5a5 5 0 0 1 5-5z" fill="none" stroke="#fff"/><circle cx="5" cy="5" r="1.6" fill="#fff"/></svg>48 Harbourline Walk<br>City, singapore<br>Zip :1234</div>
    <div><svg width="12" height="12" viewBox="0 0 12 12"><path d="M2 1l3 2-1 2c1 2 2 3 3 3l2-1 2 3-2 1C5 11 1 7 1 3z" fill="none" stroke="#fff"/></svg>+65 6100 2211</div>
    <div><svg width="14" height="10" viewBox="0 0 14 10"><rect x=".5" y=".5" width="13" height="9" fill="none" stroke="#fff"/><path d="M.5 .5l6.5 5 6.5-5" fill="none" stroke="#fff"/></svg>contact@novahomes.example</div>
  </div>
  <h4 style="left:847px">Subscribe</h4>
  <span class="sub-l">Subscribe For Our Newsletter</span>
  <div class="sub">Email Address<b>Subscribe</b></div>
  <div class="social"><i></i><i></i><i></i><i></i><i></i></div>
</footer>

<div class="abs bottom" style="left:0;width:1200px">
  <span style="left:119px">CopyRight &copy; 2018 NOVA REAL ESTATE. All Right Reserve</span>
  <span style="right:119px">Privacy Policy - Terms &amp; Conditions</span>
</div>

</body>
</html>
```